Used Car Dealer seeks an Amazing Business Card Design

We are looking for a business card design that incorporates our logo and grabs the attention of anyone we give the business card to.

Looking to use the same colors as the logo. Our Logo choice is the black background with Red and Silver/Grey Lettering.

We also would like to see some embossed designs.

Target Market(s)

Used Car Buyers, Automotive, Auto

Industry/Entity Type

Automotive

Contact Information for Business Card

BVEL7K
Gordon Whitlock
482 Tarrow Lane
Suite 207
Roswell, GA 30075
Office (770) 555-0142
Cell (770) 555-0187
bvel7kga@quellmail.com
www.bvel7kga.com

Colors
ffffff
ee3036

Requirements
Must have
• Must include our logo (Black Background with Red and Silver/Grey Lettering)
Nice to have
• Embossed Design. Can be Single or Double Sided.

```html
<!DOCTYPE html>
<html lang="en">
<head>
<meta charset="utf-8">
<title>BVEL7K Business Card</title>
<link href="https://fonts.googleapis.com/css2?family=Arimo:wght@400;700&family=Bodoni+Moda:opsz,wght@6..96,700&display=swap" rel="stylesheet">
<style>
  :root {
    --page-bg: #2e2c29;
    --card-black: #050505;
    --card-dark: #121212;
    --silver-light: #f2f3f3;
    --silver-mid: #b9bdbd;
    --text-white: #ffffff;
    --brand-red: #ee3036;
    --icon-grey: #c9cccc;
  }
  * { box-sizing: border-box; margin: 0; padding: 0; }
  html, body {
    width: 1200px;
    height: 1200px;
    overflow: hidden;
    background: var(--page-bg);
  }
  .canvas {
    position: relative;
    width: 1200px;
    height: 1200px;
  }
  .card {
    position: absolute;
    left: 350px;
    top: 185px;
    width: 501px;
    height: 830px;
    background: radial-gradient(ellipse at 50% 30%, var(--card-dark) 0%, var(--card-black) 75%);
    color: var(--text-white);
    font-family: "Arimo", Arial, sans-serif;
    text-align: center;
    box-shadow: 0 10px 30px rgba(0,0,0,0.45);
  }
  .card__band {
    position: absolute;
    left: 0;
    width: 100%;
    height: 10px;
    background: linear-gradient(90deg, var(--silver-mid), var(--silver-light) 50%, var(--silver-mid));
  }
  .card__band--top { top: 0; }
  .card__band--bottom { bottom: 0; }
  .brand-name {
    position: absolute;
    left: 0;
    width: 100%;
    top: 118px;
    font-family: "Arimo", Arial, sans-serif;
    font-weight: 700;
    font-size: 58px;
    letter-spacing: 1px;
    line-height: 66px;
    color: var(--brand-red);
  }
  .person-name {
    position: absolute;
    left: 0;
    width: 100%;
    top: 296px;
    font-family: "Bodoni Moda", "Didot", serif;
    font-weight: 700;
    font-size: 37px;
    line-height: 46px;
  }
  .phones, .address {
    position: absolute;
    left: 0;
    width: 100%;
    font-size: 25px;
    line-height: 32px;
  }
  .phones { top: 403px; }
  .address { top: 490px; }
  .contact-line {
    position: absolute;
    left: 0;
    width: 100%;
    display: flex;
    justify-content: center;
    align-items: center;
    gap: 14px;
    font-size: 25px;
    line-height: 32px;
  }
  .contact-line--email { top: 603px; }
  .contact-line--web { top: 650px; }
  .contact-line svg {
    stroke: var(--icon-grey);
    fill: none;
    stroke-width: 1.8;
  }
</style>
</head>
<body>
<div class="canvas">
  <div class="card">
    <div class="card__band card__band--top"></div>

    <div class="brand-name">BVEL7K</div>

    <div class="person-name">Gordon Whitlock</div>

    <div class="phones">
      <div>Office (770) 555-0142</div>
      <div>Cell (770) 555-0187</div>
    </div>

    <div class="address">
      <div>482 Tarrow Lane</div>
      <div>Suite 207, Roswell, GA 30075</div>
    </div>

    <div class="contact-line contact-line--email">
      <svg width="28" height="22" viewBox="0 0 28 22" aria-hidden="true">
        <rect x="1.5" y="2" width="25" height="18"/>
        <polyline points="1.5,2 14,13 26.5,2"/>
      </svg>
      <span>bvel7kga@quellmail.com</span>
    </div>

    <div class="contact-line contact-line--web">
      <svg width="30" height="30" viewBox="0 0 30 30" aria-hidden="true">
        <circle cx="15" cy="15" r="13"/>
        <ellipse cx="15" cy="15" rx="6" ry="13"/>
        <line x1="2" y1="15" x2="28" y2="15"/>
        <path d="M4.5 8 H25.5 M4.5 22 H25.5"/>
      </svg>
      <span>www.bvel7kga.com</span>
    </div>

    <div class="card__band card__band--bottom"></div>
  </div>
</div>
</body>
</html>
```